Business Card Design

We sell fish products to corporate food companies who then turn these products into final food products for consumers

Industry/Entity Type

Business

Contact Information for Business Card

I need a corporate business card template for a fish products business. We would like it be professional for use in dealing with multi national companies. This company business card template will be used by multiple employees so the following fields must be open to edit (Name, Phone Number and Email address)

```html
<!DOCTYPE html>
<html lang="en">
<head>
<meta charset="utf-8">
<title>Tidewater Seafoods – Business Card</title>
<link href="https://fonts.googleapis.com/css2?family=Roboto:wght@400;500&display=swap" rel="stylesheet">
<style>
  :root {
    --backdrop: #6b6c70;
    --card: #ffffff;
    --cyan: #1eb4dc;
    --navy: #0e57a6;
    --brand-blue: #1a5fae;
    --tab: #3cb8e4;
    --green: #62c18e;
    --green-text: #4cae74;
    --divider: #c9ccd1;
  }
  * { margin: 0; padding: 0; box-sizing: border-box; }
  html, body {
    width: 1200px; height: 873px; overflow: hidden;
    background: var(--backdrop);
    font-family: "Roboto", sans-serif;
  }
  .card {
    position: absolute; left: 380px; top: 52px;
    width: 440px; height: 770px;
    background: var(--card);
    box-shadow: 0 12px 30px rgba(0,0,0,.35);
    overflow: hidden;
  }
  .card__top-band { height: 26px; background: var(--cyan); }
  .brand {
    margin-top: 120px;
    display: flex; align-items: center; justify-content: center; gap: 12px;
  }
  .brand__dot { width: 30px; height: 30px; border-radius: 50%; background: var(--cyan); }
  .brand__name {
    font-weight: 500; font-size: 30px; letter-spacing: 1px;
    color: var(--brand-blue); text-transform: uppercase;
  }
  .person { margin-top: 84px; text-align: center; }
  .person__name { font-weight: 500; font-size: 22px; color: var(--brand-blue); letter-spacing: .5px; }
  .person__role { font-size: 16px; color: var(--green-text); letter-spacing: .5px; margin-top: 2px; }
  .contacts { margin-top: 54px; border-top: 2px solid var(--divider); }
  .contact {
    display: flex; align-items: center;
    height: 46px; background: var(--navy);
    border-bottom: 3px solid var(--divider);
    color: #fff; font-size: 17px; letter-spacing: .8px;
  }
  .contact__tab {
    width: 56px; height: 100%; flex: none;
    background: var(--tab);
    clip-path: polygon(0 0, 78% 0, 100% 50%, 78% 100%, 0 100%);
    display: flex; align-items: center; justify-content: center; padding-right: 10px;
  }
  .contact__tab svg { width: 20px; height: 20px; }
  .contact__text { margin-left: 14px; }
  .card__footer {
    position: absolute; left: 0; right: 0; bottom: 0; height: 62px;
    background: var(--green);
    display: flex; align-items: center; justify-content: center;
    color: #eef9f2; font-size: 17px; letter-spacing: .5px;
  }
</style>
</head>
<body>
  <main class="card">
    <div class="card__top-band"></div>

    <div class="brand">
      <span class="brand__dot"></span>
      <span class="brand__name">Tidewater Seafoods</span>
    </div>

    <div class="person">
      <div class="person__name">Marla Venn</div>
      <div class="person__role">General Manager</div>
    </div>

    <ul class="contacts" style="list-style:none">
      <li class="contact">
        <span class="contact__tab">
          <svg viewBox="0 0 20 20" fill="none" stroke="#fff" stroke-width="1.8"><rect x="5" y="2" width="10" height="16" rx="2"/><line x1="8" y1="15" x2="12" y2="15"/></svg>
        </span>
        <span class="contact__text">555.014.2290</span>
      </li>
      <li class="contact">
        <span class="contact__tab">
          <svg viewBox="0 0 20 20" fill="none" stroke="#fff" stroke-width="1.8"><rect x="2" y="5" width="16" height="11" rx="1"/><polyline points="2,5 10,11 18,5"/></svg>
        </span>
        <span class="contact__text">marla_venn@example.com</span>
      </li>
      <li class="contact">
        <span class="contact__tab">
          <svg viewBox="0 0 20 20" fill="none" stroke="#fff" stroke-width="1.6"><circle cx="10" cy="10" r="8"/><ellipse cx="10" cy="10" rx="3.5" ry="8"/><line x1="2" y1="10" x2="18" y2="10"/></svg>
        </span>
        <span class="contact__text">www.tidewaterseafoods.com</span>
      </li>
      <li class="contact">
        <span class="contact__tab">
          <svg viewBox="0 0 20 20" fill="none" stroke="#fff" stroke-width="1.8"><path d="M10 18 C5 12 4 10 4 8 a6 6 0 0 1 12 0 c0 2-1 4-6 10z"/><circle cx="10" cy="8" r="2"/></svg>
        </span>
        <span class="contact__text">Port Alder, CA 94000</span>
      </li>
    </ul>

    <footer class="card__footer">Lorem Ipsum Dolor Lorem Ipsum</footer>
  </main>
</body>
</html>
```